Business Card Design Project

KV Strategy Partners is a management consulting business with C-suite (CEO/CFO etc) target clients. Logo selected is blue with simple/serious typefaces.

Target Market(s)

CEOs and CFOs of large corporates

Industry/Entity Type

Management Consulting

Font styles to use
Serif

Colors
3276b5

Requirements
Must have
• Tag line: Building successful collaborations (use different font)
Address: 457 Cedar Brook Lane #03-22 Singapore 519307
Telephone: +65 8372 6094
Email: kvlorne@mailbox47.com

```html
<!DOCTYPE html>
<html lang="en">
<head>
<meta charset="utf-8">
<title>KV Strategy Partners – Business Card</title>
<link rel="stylesheet" href="https://fonts.googleapis.com/css2?family=Tinos:wght@400&family=Arimo:wght@400&display=swap">
<style>
  :root {
    --stage: #ecebe8;
    --navy: #1d3a66;
    --navy-deep: #142b4f;
    --navy-light: #2a4c80;
    --ink: #141414;
    --paper: #ffffff;
    --rule: #9a9a9a;
  }
  * { margin: 0; padding: 0; box-sizing: border-box; }
  html, body {
    width: 1200px;
    height: 784px;
    overflow: hidden;
    background: var(--stage);
  }
  .canvas {
    position: relative;
    width: 1200px;
    height: 784px;
    display: flex;
    align-items: center;
    justify-content: center;
    gap: 40px;
  }
  .card {
    position: relative;
    width: 540px;
    height: 310px;
    box-shadow: 0 6px 18px rgba(0,0,0,0.18);
    overflow: hidden;
  }

  /* Front side */
  .card-front {
    background: var(--paper);
    font-family: "Tinos", "Times New Roman", serif;
    color: var(--ink);
  }
  .brand {
    position: absolute;
    left: 40px;
    top: 48px;
    font-size: 40px;
    line-height: 1;
    color: var(--navy);
    letter-spacing: 0.5px;
  }
  .contact-list {
    position: absolute;
    left: 40px;
    bottom: 34px;
    list-style: none;
    font-size: 19px;
    line-height: 1.3;
  }
  .contact-item {
    display: flex;
    align-items: flex-start;
    gap: 8px;
  }
  .contact-icon {
    width: 16px;
    height: 16px;
    margin-top: 4px;
    flex: none;
    fill: var(--navy);
  }
  .contact-address { display: block; }

  /* Back side */
  .card-back {
    background: radial-gradient(ellipse at 40% 35%, var(--navy-light) 0%, var(--navy) 55%, var(--navy-deep) 100%);
  }
  .tagline {
    position: absolute;
    left: 0;
    right: 0;
    top: 50%;
    transform: translateY(-50%);
    text-align: center;
    font-family: "Arimo", Arial, sans-serif;
    font-size: 15px;
    letter-spacing: 5px;
    color: var(--paper);
  }
</style>
</head>
<body>
<main class="canvas">

  <section class="card card-front" aria-label="Business card front">
    <div class="brand">KV Strategy Partners</div>

    <ul class="contact-list">
      <li class="contact-item">
        <svg class="contact-icon" viewBox="0 0 16 16" aria-hidden="true">
          <path d="M3.2 1.2l2.4 2.6-1.3 1.8c.9 2 2.2 3.3 4.1 4.2l1.8-1.3 2.6 2.4-1.3 2.3C6.6 13.3 2.7 9.4 1 4.1z"/>
        </svg>
        <span>+65 8372 6094</span>
      </li>
      <li class="contact-item">
        <svg class="contact-icon" viewBox="0 0 16 16" aria-hidden="true">
          <path d="M1 3.5h14v9H1z M1.8 4.3L8 9l6.2-4.7" fill="none" stroke="currentColor" stroke-width="1.4" style="stroke:var(--navy)"/>
        </svg>
        <span>kvlorne@mailbox47.com</span>
      </li>
      <li class="contact-item">
        <svg class="contact-icon" viewBox="0 0 16 16" aria-hidden="true">
          <path d="M8 1.5L1 7.8h2V14.5h3.8v-4h2.4v4H13V7.8h2z"/>
        </svg>
        <span class="contact-address">457 Cedar Brook Lane #03-22<br>Singapore 519307</span>
      </li>
    </ul>
  </section>

  <section class="card card-back" aria-label="Business card back">
    <p class="tagline">Building successful collaborations</p>
  </section>

</main>
</body>
</html>
```